Corvix Energy Battery advertisment for Facebook ads

Objective:
Design a compelling Facebook advertisement to promote the new Federal Government Home Battery Subsidy, encouraging existing solar customers to act now and install a battery system under the new subsidy program.

Key Message:

25kWh Battery System Installed from $9,800
Act now and secure your affordable energy future today!
Design Requirements:

Bold headline showcasing the 25kWh for $9,800 offer.
Clear reference to the Federal Government Battery Subsidy as the reason for the low pricing.
Include messaging around:
Claim your subsidy before it winds down—like the solar rebate, it reduces each year
The subsidy can only be claimed once per household—go large now to future-proof your energy needs
Add a strong Call to Action like: “Beat the Rush—Secure Your Battery Today!”

Target Market(s)

Home owners who want to add batteries to existing solar systems

Industry/Entity Type

Renewable energy

Colors
0054AA
0677BA
7BADD7
CADEEF
E8F1F8
EB3D1F
EC4F4E
F09395
F8D3D4
FCEDEE

Requirements
Must have
• Visual Style: Modern, clean, and high-trust Use imagery of solar homes, battery units, or families enjoying power security at night Include visual cues of savings, energy independence, or clean energy Mobile-optimized, designed for Facebook feed
Nice to have
• Tone: Confident, future-focused, and urgent—while remaining trustworthy and informative. I would like a picture of battery ideally TQM battery on a home or such
Should not have
• must be professional and be a call to action

```html
<!DOCTYPE html>
<html lang="en">
<head>
<meta charset="utf-8">
<title>Corvix Energy – 25kWh Battery Offer</title>
<link rel="stylesheet" href="https://fonts.googleapis.com/css2?family=Anton&family=Oswald:wght@600;700&family=Montserrat:ital,wght@0,600;0,700;0,800;1,800;1,900&display=swap">
<style>
  :root{
    --navy:#0b1f6e;
    --blue-deep:#0054AA;
    --blue:#0677BA;
    --blue-sky:#20b7f0;
    --blue-soft:#7BADD7;
    --blue-pale:#CADEEF;
    --blue-mist:#E8F1F8;
    --red:#b81c26;
    --red-dark:#7d0d14;
    --orange:#f47a1f;
    --white:#ffffff;
    --ink:#111111;
  }
  *{margin:0;padding:0;box-sizing:border-box}
  html,body{width:1200px;height:988px;overflow:hidden;background:var(--white)}
  .ad{position:relative;width:1200px;height:988px;overflow:hidden;font-family:"Montserrat",sans-serif;color:var(--white)}
  .scene-photo{position:absolute;inset:0;
    background:
      radial-gradient(ellipse 420px 260px at 160px 90px,rgba(255,255,255,.95),rgba(255,255,255,0) 70%),
      linear-gradient(180deg,#6f86b8 0%,#a9b8d6 18%,#8fb6dc 38%,#2fa6e4 58%,#0a86d8 72%,#0b6fc8 100%);}
  .corner-stripes{position:absolute;top:0;right:0;width:310px;height:230px}
  .brand{position:absolute;left:83px;top:58px;display:flex;flex-direction:column;gap:10px}
  .brand-row{display:flex;align-items:center;gap:12px}
  .brand-dot{width:26px;height:26px;border-radius:50%;background:var(--blue-deep)}
  .brand-name{font-family:"Oswald",sans-serif;font-weight:600;font-size:44px;line-height:1;color:var(--navy);letter-spacing:1px}
  .brand-tag{font-size:12.5px;font-weight:600;color:#2a3550;letter-spacing:.2px}
  .headline{position:absolute;left:70px;top:206px;font-family:"Anton",sans-serif;font-size:124px;line-height:1;color:var(--navy);
    -webkit-text-stroke:10px var(--white);paint-order:stroke fill;letter-spacing:-1px;
    filter:drop-shadow(0 0 6px rgba(40,190,255,.9)) drop-shadow(0 4px 4px rgba(0,0,60,.35))}
  .price-label{position:absolute;right:816px;top:382px;text-align:right;font-family:"Oswald",sans-serif;font-weight:700;font-size:40px;line-height:1.15;color:var(--white);
    text-shadow:0 3px 4px rgba(0,20,80,.6)}
  .price-box{position:absolute;left:398px;top:371px;width:318px;height:119px;border-radius:16px;border:3px solid #5fd3ff;
    background:linear-gradient(180deg,#1fa4ee 0%,#0a4fb0 55%,#0b2f8c 100%);display:flex;align-items:center;justify-content:center;
    box-shadow:0 0 10px rgba(90,210,255,.7)}
  .price-value{font-family:"Anton",sans-serif;font-size:86px;color:var(--white);text-shadow:0 4px 4px rgba(0,0,50,.55)}
  .tagline{position:absolute;left:40px;width:770px;top:508px;text-align:center;font-weight:900;font-style:italic;font-size:28.5px;line-height:1.55;
    color:var(--white);text-shadow:2px 3px 0 rgba(0,40,110,.55)}
  .battery-photo{position:absolute;left:884px;top:112px;width:282px;height:508px;border-radius:6px;
    background:linear-gradient(90deg,#d5d8db 0%,#f4f5f6 12%,#ffffff 55%,#e4e6e8 100%)}
  .red-band{position:absolute;left:0;top:600px;width:1200px;height:388px}
  .feature-icons{position:absolute;left:270px;top:612px;width:320px;height:96px}
  .benefits{position:absolute;left:40px;width:772px;top:738px;text-align:center;font-weight:600;font-size:21.5px;line-height:31px;text-transform:uppercase;letter-spacing:.2px}
  .cta-side{position:absolute;right:39px;top:716px;text-align:right;font-family:"Oswald",sans-serif;font-weight:700;font-size:56px;line-height:1.05;letter-spacing:-.5px}
  .social{position:absolute;left:978px;top:857px;width:180px;text-align:center}
  .social-title,.social-name{font-weight:800;font-style:italic;font-size:18px}
  .social-dots{display:flex;justify-content:center;gap:16px;margin:9px 0 6px}
  .social-dots span{width:40px;height:40px;border-radius:50%;background:radial-gradient(circle at 40% 35%,#ff3b3b,#c40d12)}
  .book{position:absolute;left:49px;top:911px;display:flex;height:48px}
  .book-label{background:var(--white);color:var(--ink);font-weight:900;font-style:italic;font-size:31px;padding:0 18px;border-radius:10px 0 0 10px;display:flex;align-items:center;letter-spacing:-1px}
  .book-arrow{width:47px;background:var(--orange);border-radius:0 10px 10px 0;display:flex;align-items:center;justify-content:center}
  .contact{position:absolute;top:916px;display:flex;align-items:center;gap:10px}
  .contact.phone{left:345px}
  .contact.web{left:606px}
  .contact-small{font-size:13px;font-weight:700;line-height:1}
  .contact-big{font-size:24px;font-weight:800;line-height:1.15}
</style>
</head>
<body>
<div class="ad">
  <div class="scene-photo" role="img" aria-label="Suburban home with solar panels on the roof under a blue sky"></div>

  <svg class="corner-stripes" viewBox="0 0 310 230" aria-hidden="true">
    <polygon points="0,0 80,0 310,150 310,210" fill="#ffffff" opacity=".9"/>
    <polygon points="180,0 310,0 310,80" fill="#1a3d9a"/>
    <polygon points="150,92 205,92 310,175 310,225" fill="#10308a"/>
  </svg>

  <div class="brand">
    <div class="brand-row">
      <div class="brand-dot"></div>
      <div class="brand-name">CORVIX ENERGY</div>
    </div>
    <div class="brand-tag">SMART POWER AND STORAGE FOR HOMES</div>
  </div>

  <div class="headline">25kWh Battery</div>

  <div class="price-label">System<br>Installed from</div>
  <div class="price-box"><span class="price-value">$9,800</span></div>

  <p class="tagline">ACT NOW AND SECURE YOUR AFFORDABLE<br>ENERGY FUTURE TODAY!</p>

  <div class="battery-photo" role="img" aria-label="White stacked TQM home battery unit on feet"></div>

  <svg class="red-band" viewBox="0 0 1200 388" aria-hidden="true">
    <defs>
      <linearGradient id="bandFill" x1="0" y1="0" x2="0" y2="1">
        <stop offset="0" stop-color="#c11f2a"/>
        <stop offset="1" stop-color="#8e1017"/>
      </linearGradient>
    </defs>
    <path d="M0,118 C260,40 620,20 860,28 C1000,34 1120,60 1200,84 L1200,388 L0,388 Z" fill="#6a0a10"/>
    <path d="M0,132 C260,54 620,34 860,42 C1000,48 1120,74 1200,98 L1200,388 L0,388 Z" fill="url(#bandFill)"/>
  </svg>

  <svg class="feature-icons" viewBox="0 0 320 96" aria-hidden="true">
    <defs>
      <radialGradient id="iconFill" cx=".4" cy=".35" r=".7">
        <stop offset="0" stop-color="#2fb0f2"/>
        <stop offset="1" stop-color="#0b3f9c"/>
      </radialGradient>
    </defs>
    <g stroke="#ffffff" stroke-width="3">
      <circle cx="47" cy="48" r="45" fill="url(#iconFill)"/>
      <circle cx="153" cy="48" r="45" fill="url(#iconFill)"/>
      <circle cx="264" cy="48" r="45" fill="url(#iconFill)"/>
    </g>
    <path d="M20,50 L47,26 L74,50 L67,50 L67,72 L54,72 L54,58 L40,58 L40,72 L27,72 L27,50 Z" fill="#ffffff"/>
    <g fill="none" stroke="#ffffff" stroke-width="3" stroke-linecap="round">
      <path d="M133,62 A25,25 0 0 1 150,24"/>
      <path d="M173,34 A25,25 0 0 1 158,72"/>
      <path d="M245,60 A24,24 0 0 1 278,28"/>
      <path d="M283,36 A24,24 0 0 1 250,68"/>
    </g>
    <path d="M155,22 C168,18 174,26 170,32 C162,30 156,28 155,22 Z" fill="#ffffff"/>
    <rect x="160" y="68" width="12" height="10" fill="#ffffff"/>
    <path d="M270,28 L256,52 L265,52 L259,70 L275,44 L266,44 Z" fill="#ffffff"/>
  </svg>

  <div class="benefits">
    Claim your subsidy before it winds down<br>
    Like the solar rebate, it reduces each year<br>
    The subsidy can only be claimed once per household<br>
    Go large now to future-proof your energy needs
  </div>

  <div class="cta-side">Secure Your<br>Battery Today!</div>

  <div class="social">
    <div class="social-title">Watc Us Work</div>
    <div class="social-dots"><span></span><span></span><span></span></div>
    <div class="social-name">Corvix Energy</div>
  </div>

  <div class="book">
    <div class="book-label">BOOK NOW!</div>
    <div class="book-arrow">
      <svg width="24" height="30" viewBox="0 0 24 30" aria-hidden="true"><path d="M5,3 L19,15 L5,27" fill="none" stroke="#ffffff" stroke-width="5" stroke-linecap="round" stroke-linejoin="round"/></svg>
    </div>
  </div>

  <div class="contact phone">
    <svg width="40" height="40" viewBox="0 0 40 40" aria-hidden="true">
      <path d="M10,4 L16,12 L12,16 C14,22 18,26 24,28 L28,24 L36,30 L32,36 C18,36 4,22 4,8 Z" fill="none" stroke="#ffffff" stroke-width="3" stroke-linejoin="round"/>
      <path d="M24,4 A12,12 0 0 1 36,16 M24,10 A6,6 0 0 1 30,16" fill="none" stroke="#ffffff" stroke-width="2.5" stroke-linecap="round"/>
    </svg>
    <div>
      <div class="contact-small">Call to find out more</div>
      <div class="contact-big">+61 7 3000 4821</div>
    </div>
  </div>

  <div class="contact web">
    <svg width="40" height="40" viewBox="0 0 40 40" aria-hidden="true">
      <g fill="none" stroke="#ffffff" stroke-width="2.5">
        <circle cx="18" cy="18" r="15"/>
        <ellipse cx="18" cy="18" rx="6" ry="15"/>
        <path d="M3,18 H33 M6,10 H30 M6,26 H24"/>
      </g>
      <path d="M25,25 L37,31 L31,33 L29,39 Z" fill="#ffffff"/>
    </svg>
    <div>
      <div class="contact-small">Visit Our Website</div>
      <div class="contact-big">corvixenergy.com.au</div>
    </div>
  </div>
</div>
</body>
</html>
```